Webdesign für Importeur von Tierbedarfsartikeln
Zielgruppe
Wir importieren Tierbedarfsartikel und verkaufen sie ausschließlich online. Zielgruppe sind in erster Linie Katzenhalter.
Aufgabenstellung
Es gibt eine bestehende Webseite www.pfotenhain-shop.de Sie wurde bei Nevrix erstellt und ist aktiv. Die Seite soll eine professionelle Ansicht erhalten. Schön wären edle Farben, nicht kunterbunt. Wichtig in dem Zusammenhang ist eben, dass sich derjenige mit dem Nevrixkonzept auskennt.
Dieser Auftrag wird Folgeaufträge erhalten, sprich Logo, Werbeflyer usw. Bilder der Produkte sind vorhanden.

```html
<!DOCTYPE html>
<html lang="de">
<head>
<meta charset="utf-8">
<title>Pfotenhain – Startseite</title>
<link href="https://fonts.googleapis.com/css2?family=Outfit:wght@300;400;500;600&family=Poppins:wght@300;400;500;600&display=swap" rel="stylesheet">
<style>
:root{
  --ink:#111;
  --navy:#0f1b26;
  --brand:#0b6f90;
  --orange:#f0a020;
  --star:#f0a21a;
  --badge:#f26b2a;
  --line:#9a9a9a;
  --white:#fff;
}
*{box-sizing:border-box;margin:0;padding:0}
html,body{width:679px;height:1200px;overflow:hidden;background:var(--white)}
body{font-family:"Outfit",sans-serif;color:var(--ink);position:relative}
.abs{position:absolute}

.promo-bar{left:0;top:0;width:679px;height:23px;background:var(--navy);color:var(--white);font-size:8.4px;display:flex;align-items:center;justify-content:center;gap:20px;padding-left:70px;z-index:2}
.promo-item{display:flex;align-items:center;gap:9px;white-space:nowrap}

.site-header{left:0;top:23px;width:679px;height:42px;background:var(--brand);z-index:1}
.brand-name{left:68px;top:44px;font-family:"Outfit",sans-serif;font-weight:500;font-size:12px;line-height:14px;color:var(--white);display:flex;align-items:center;gap:4px;z-index:2}
.brand-dot{width:6px;height:6px;background:var(--white);border-radius:50%}
.main-nav{top:38px;font-size:8.6px;line-height:12px;font-weight:600;color:var(--white);z-index:2;white-space:nowrap}
.main-nav.active{color:var(--orange);font-weight:400}
.nav-icons{left:569px;top:39px;display:flex;gap:6px;align-items:center;z-index:2}
.cart-badge{left:598px;top:35px;width:10px;height:10px;border-radius:50%;background:var(--badge);color:#fff;font-size:7px;text-align:center;line-height:10px;z-index:3}

.dropdown{left:434px;top:65px;width:94px;height:99px;background:var(--brand);z-index:3;padding-top:3px}
.dropdown li{list-style:none;color:var(--white);font-size:8.2px;height:19.5px;line-height:19.5px;padding-left:9px;letter-spacing:-0.1px;white-space:nowrap}

.hero-visual{left:210px;top:65px;width:469px;height:257px;background:
  radial-gradient(ellipse at 55% 60%, #8f8c89 0%, #b6b3b0 30%, rgba(230,228,226,0.8) 60%, rgba(255,255,255,0) 85%),
  linear-gradient(90deg,#fff 0%,#efedeb 30%,#e3e1df 70%,#f3f2f1 100%)}
.hero-kicker{left:67px;top:108px;font-size:8px;color:#444;font-weight:300}
.hero-title{left:67px;top:118px;font-size:21px;font-weight:600;color:var(--brand);letter-spacing:-0.2px}
.hero-copy{left:67px;top:156px;width:280px;font-size:8px;line-height:12.5px;color:#444;font-weight:300}
.hero-copy p{margin-bottom:11.5px}
.btn-outline{border:1px solid var(--brand);border-radius:3px;color:var(--brand);font-size:8.4px;font-weight:500;display:flex;align-items:center;justify-content:center;background:#fff}

.section-title{left:64px;font-size:20.5px;font-weight:400;letter-spacing:-0.2px}
.section-rule{left:199px;width:409px;height:1px;background:var(--line)}
.carousel-arrow{width:15px;height:15px}

.product-card{width:117px;height:175px;background:#fff;box-shadow:0 0.5px 3px rgba(0,0,0,0.18)}
.product-photo{position:absolute;left:12px;top:13px;width:94px;height:94px}
.product-name{position:absolute;left:12px;top:112px;width:96px;font-size:7.1px;line-height:10px;color:#555;font-weight:300}
.product-rating{position:absolute;left:12px;display:flex;align-items:center;gap:2.5px;font-size:7.2px;color:#555}
.product-price{position:absolute;left:12px;font-size:10.4px;font-weight:500;color:#222}

.site-footer{left:0;top:960px;width:679px;height:240px;background:var(--navy);color:var(--white);font-family:"Poppins",sans-serif}
.footer-brand{left:64px;top:42px;font-size:20px;font-weight:600}
.footer-line{font-size:8px;font-weight:300;display:flex;align-items:center;gap:7px;white-space:nowrap}
</style>
</head>
<body>
<svg width="0" height="0" style="position:absolute">
  <defs>
    <symbol id="star-full" viewBox="0 0 24 24"><path d="M12 2l3 6.9 7.5.7-5.7 5 1.7 7.4L12 18.2 5.5 22l1.7-7.4-5.7-5 7.5-.7z" fill="var(--star)"/></symbol>
    <symbol id="star-empty" viewBox="0 0 24 24"><path d="M12 2l3 6.9 7.5.7-5.7 5 1.7 7.4L12 18.2 5.5 22l1.7-7.4-5.7-5 7.5-.7z" fill="none" stroke="var(--star)" stroke-width="1.8"/></symbol>
    <symbol id="arrow-left" viewBox="0 0 24 24"><circle cx="12" cy="12" r="10.5" fill="none" stroke="#777" stroke-width="1.3"/><path d="M13.5 7.5L9 12l4.5 4.5" fill="none" stroke="#777" stroke-width="1.3"/></symbol>
    <symbol id="arrow-right" viewBox="0 0 24 24"><circle cx="12" cy="12" r="10.5" fill="none" stroke="#777" stroke-width="1.3"/><path d="M10.5 7.5L15 12l-4.5 4.5" fill="none" stroke="#777" stroke-width="1.3"/></symbol>
  </defs>
</svg>

<div class="abs promo-bar">
  <div class="promo-item">
    <svg width="16" height="9" viewBox="0 0 16 9"><rect x="0.5" y="0.5" width="15" height="8" rx="1" fill="none" stroke="#fff"/><circle cx="8" cy="4.5" r="2" fill="#fff"/></svg>
    <span>Gutscheincode "Plüsch" und 15% auf alle Kuschelbetten sichern</span>
  </div>
  <div class="promo-item">
    <svg width="15" height="10" viewBox="0 0 15 10"><path d="M1 3h13v6H1z M1 3l3-2h7l3 2" fill="#fff"/></svg>
    <span>Kostenloser Versand ab €65,00</span>
  </div>
</div>

<header class="abs site-header"></header>
<div class="abs brand-name"><span class="brand-dot"></span>Pfotenhain</div>
<span class="abs main-nav" style="left:374px">Pfotenhain</span>
<span class="abs main-nav active" style="left:434px">Products ▾</span>
<span class="abs main-nav" style="left:485px">Sale</span>
<span class="abs main-nav" style="left:517px">Kontakt</span>
<div class="abs nav-icons">
  <svg width="12" height="12" viewBox="0 0 24 24"><circle cx="12" cy="12" r="11" fill="#fff"/><circle cx="12" cy="9" r="4" fill="var(--brand)"/><path d="M5 19c2-4 12-4 14 0" fill="var(--brand)"/></svg>
  <svg width="14" height="12" viewBox="0 0 24 20"><path d="M1 2h4l3 11h12l2-8H7" fill="none" stroke="#fff" stroke-width="2"/><circle cx="10" cy="17" r="1.8" fill="#fff"/><circle cx="18" cy="17" r="1.8" fill="#fff"/></svg>
</div>
<div class="abs cart-badge">5</div>

<ul class="abs dropdown">
  <li>Katzenkratzartikel</li>
  <li>Plüschbetten</li>
  <li>Katzenspielzeug</li>
  <li>Interaktive Spielzeuge</li>
  <li>Zubehör</li>
</ul>

<div class="abs hero-visual" role="img" aria-label="Kätzchen schaut aus einer Papiertüte"></div>
<div class="abs hero-kicker">WILLKOMMEN BEI</div>
<h1 class="abs hero-title">Pfotenhain.de</h1>
<div class="abs hero-copy">
  <p>Hier findest Du eine liebevoll zusammengestellte Auswahl an<br>Zubehör für deine vierbeinigen Familienmitglieder.</p>
  <p>Unsere Artikel wurden durch unser qualifiziertes, flauschiges Fachpersonal auf Haltbarkeit und Spielspaß geprüft und sind mit schnurrigen Grüßen zu empfehlen!</p>
  <p>Schön, dass du da bist!</p>
</div>
<a class="abs btn-outline" style="left:67px;top:268px;width:55px;height:16px">KONTAKT</a>

<h2 class="abs section-title" style="top:369px">Top-Produkte</h2>
<div class="abs section-rule" style="top:382px"></div>
<svg class="abs carousel-arrow" style="left:63px;top:455px"><use href="#arrow-left"/></svg>
<svg class="abs carousel-arrow" style="left:600px;top:455px"><use href="#arrow-right"/></svg>

<div class="abs product-card" style="left:93px;top:416px">
  <div class="product-photo" role="img" aria-label="Rot-schwarze Spielschlange auf Holzboden" style="background:linear-gradient(160deg,#f2c9c0 0%,#d9a57c 45%,#c98e5e 100%)"></div>
  <div class="product-name">Interaktive Spielschlange</div>
  <div class="product-rating" style="top:137px"><svg width="9" height="9"><use href="#star-full"/></svg><svg width="9" height="9"><use href="#star-full"/></svg><svg width="9" height="9"><use href="#star-full"/></svg><svg width="9" height="9"><use href="#star-full"/></svg><svg width="9" height="9"><use href="#star-empty"/></svg>&nbsp;100</div>
  <div class="product-price" style="top:150px">19,99 €</div>
</div>
<div class="abs product-card" style="left:218px;top:416px">
  <div class="product-photo" role="img" aria-label="Rosa Katzenhöhle auf Fell" style="background:linear-gradient(160deg,#b9b7b5 0%,#e5c7d8 50%,#d9d7d5 100%)"></div>
  <div class="product-name">Interaktive Spielschlange</div>
  <div class="product-rating" style="top:137px"><svg width="9" height="9"><use href="#star-full"/></svg><svg width="9" height="9"><use href="#star-full"/></svg><svg width="9" height="9"><use href="#star-full"/></svg><svg width="9" height="9"><use href="#star-full"/></svg><svg width="9" height="9"><use href="#star-empty"/></svg>&nbsp;100</div>
  <div class="product-price" style="top:150px">19,99 €</div>
</div>
<div class="abs product-card" style="left:344px;top:416px">
  <div class="product-photo" role="img" aria-label="Bunte Plüschmäuse mit Katzenminze-Fläschchen" style="background:linear-gradient(150deg,#5aa0d0 0%,#e58a3c 35%,#8fbf5a 60%,#8a3f8f 100%)"></div>
  <div class="product-name">Plüschmäuse in vier Farben mit Katzenminze</div>
  <div class="product-rating" style="top:138px"><svg width="9" height="9"><use href="#star-full"/></svg><svg width="9" height="9"><use href="#star-full"/></svg><svg width="9" height="9"><use href="#star-full"/></svg><svg width="9" height="9"><use href="#star-full"/></svg><svg width="9" height="9"><use href="#star-empty"/></svg>&nbsp;84</div>
  <div class="product-price" style="top:151px">ab 4,19 €</div>
</div>
<div class="abs product-card" style="left:470px;top:416px">
  <div class="product-photo" role="img" aria-label="Katze spielt mit weißem Drehspielzeug" style="background:linear-gradient(160deg,#8a8784 0%,#b8b5b2 50%,#e6e4e2 100%)"></div>
  <div class="product-name">FelixPlay Running Smart</div>
  <div class="product-rating" style="top:138px"><svg width="9" height="9"><use href="#star-full"/></svg><svg width="9" height="9"><use href="#star-full"/></svg><svg width="9" height="9"><use href="#star-full"/></svg><svg width="9" height="9"><use href="#star-full"/></svg><svg width="9" height="9"><use href="#star-empty"/></svg>&nbsp;84</div>
  <div class="product-price" style="top:151px">21,99 €</div>
</div>
<a class="abs btn-outline" style="left:304px;top:603px;width:71px;height:16px">ALLES SEHEN</a>

<h2 class="abs section-title" style="top:652px">Neues Produkt</h2>
<div class="abs section-rule" style="top:665px"></div>
<svg class="abs carousel-arrow" style="left:63px;top:738px"><use href="#arrow-left"/></svg>
<svg class="abs carousel-arrow" style="left:600px;top:738px"><use href="#arrow-right"/></svg>

<div class="abs product-card" style="left:93px;top:699px">
  <div class="product-photo" role="img" aria-label="Rot-schwarze Spielschlange auf Holzboden" style="background:linear-gradient(160deg,#f2c9c0 0%,#d9a57c 45%,#c98e5e 100%)"></div>
  <div class="product-name">Interaktive Spielschlange</div>
  <div class="product-rating" style="top:137px"><svg width="9" height="9"><use href="#star-full"/></svg><svg width="9" height="9"><use href="#star-full"/></svg><svg width="9" height="9"><use href="#star-full"/></svg><svg width="9" height="9"><use href="#star-full"/></svg><svg width="9" height="9"><use href="#star-empty"/></svg>&nbsp;100</div>
  <div class="product-price" style="top:150px">19,99 €</div>
</div>
<div class="abs product-card" style="left:218px;top:699px">
  <div class="product-photo" role="img" aria-label="Rosa Katzenhöhle auf Fell" style="background:linear-gradient(160deg,#b9b7b5 0%,#e5c7d8 50%,#d9d7d5 100%)"></div>
  <div class="product-name">Interaktive Spielschlange</div>
  <div class="product-rating" style="top:137px"><svg width="9" height="9"><use href="#star-full"/></svg><svg width="9" height="9"><use href="#star-full"/></svg><svg width="9" height="9"><use href="#star-full"/></svg><svg width="9" height="9"><use href="#star-full"/></svg><svg width="9" height="9"><use href="#star-empty"/></svg>&nbsp;100</div>
  <div class="product-price" style="top:150px">19,99 €</div>
</div>
<div class="abs product-card" style="left:344px;top:699px">
  <div class="product-photo" role="img" aria-label="Bunte Plüschmäuse mit Katzenminze-Fläschchen" style="background:linear-gradient(150deg,#5aa0d0 0%,#e58a3c 35%,#8fbf5a 60%,#8a3f8f 100%)"></div>
  <div class="product-name">Plüschmäuse in vier Farben mit Katzenminze</div>
  <div class="product-rating" style="top:138px"><svg width="9" height="9"><use href="#star-full"/></svg><svg width="9" height="9"><use href="#star-full"/></svg><svg width="9" height="9"><use href="#star-full"/></svg><svg width="9" height="9"><use href="#star-full"/></svg><svg width="9" height="9"><use href="#star-empty"/></svg>&nbsp;84</div>
  <div class="product-price" style="top:151px">ab 4,19 €</div>
</div>
<div class="abs product-card" style="left:470px;top:699px">
  <div class="product-photo" role="img" aria-label="Katze spielt mit weißem Drehspielzeug" style="background:linear-gradient(160deg,#8a8784 0%,#b8b5b2 50%,#e6e4e2 100%)"></div>
  <div class="product-name">FelixPlay Running Smart</div>
  <div class="product-rating" style="top:138px"><svg width="9" height="9"><use href="#star-full"/></svg><svg width="9" height="9"><use href="#star-full"/></svg><svg width="9" height="9"><use href="#star-full"/></svg><svg width="9" height="9"><use href="#star-full"/></svg><svg width="9" height="9"><use href="#star-empty"/></svg>&nbsp;84</div>
  <div class="product-price" style="top:151px">21,99 €</div>
</div>
<a class="abs btn-outline" style="left:304px;top:886px;width:71px;height:16px">ALLES SEHEN</a>

<footer class="abs site-footer">
  <div class="abs footer-brand">Pfotenhain</div>
  <div class="abs footer-line" style="left:69px;top:86px">FALKNER &amp; SÖHNE GmbH</div>
  <div class="abs footer-line" style="left:69px;top:106px">Lindenweg 12 Top3</div>
  <div class="abs footer-line" style="left:69px;top:126px">6372 Waldhofen</div>
  <div class="abs footer-line" style="left:69px;top:146px">ÖSTERREICH</div>
  <div class="abs footer-line" style="left:69px;top:167px"><svg width="11" height="9" viewBox="0 0 22 18"><rect x="1" y="1" width="20" height="16" rx="1.5" fill="none" stroke="#fff" stroke-width="1.6"/><path d="M1 2l10 8 10-8" fill="none" stroke="#fff" stroke-width="1.6"/></svg>office@falkner-soehne.at</div>
  <div class="abs footer-line" style="left:69px;top:187px"><svg width="11" height="11" viewBox="0 0 24 24"><path d="M5 2l4 4-2 3c1 3 4 6 7 7l3-2 4 4-3 4C10 21 3 14 2 5z" fill="none" stroke="#fff" stroke-width="1.5"/></svg>+43 (0) 5123 456 78</div>

  <div class="abs footer-line" style="left:465px;top:86px;font-weight:400">Impressum</div>
  <div class="abs footer-line" style="left:465px;top:106px;font-weight:400">Datenschutzerklärung</div>
  <div class="abs footer-line" style="left:465px;top:126px;font-weight:400">Cookie-Richtlinie</div>
  <div class="abs footer-line" style="left:465px;top:146px;font-weight:400">Zahlung &amp; Versand</div>
  <div class="abs footer-line" style="left:465px;top:166px;font-weight:400">Allgemeine Geschäftsbedingungen</div>
  <div class="abs footer-line" style="left:465px;top:185px;font-weight:400">Widerrufsrecht</div>
</footer>
</body>
</html>
```